Holistic Therapy (aromatherapy, massage, reflexology, life coaching, soul healing, aura reading)

I work for myself as a holistic therapist doing: aromatherapy massage, massage, reflexology, abdominal-sacral massage, life coaching, soul healing, aura readings. I want a business card that doesn't focus on any one of these( so not just feet or a massage couch,but rather a card that creates the feeling of wholeness, healing, health and which can encompass all my therapies - e.g. green or purple are colours I like (especially green, or maybe green on back and purple on front). It's going to be called Rosa Pell Therapies. I don't want to list all my therapies on the card in case I add others later.). At some point I will create a website but in this instance I just want to get some cards printed to get 'out there' while I design my website.

Hi, thanks for all your designs. Can you find a way to include the therapies that I offer within the card, either on the front or back…the therapies I offer are: aromatherapy massage, reflexology, swedish body massage, abdominal-sacral massage, nutrition, soul healing, aura readings. (Maybe have them with a bullet point before each?) I am not sure whether they should be on the front of the card or the back or whether having them would spoil the card but it occurred to me that just having rosa pell therapies doesn't tell people what therapies I offer, hence the new idea to list them somehow…)

Target Market(s)

Mainly women (middle class probably with disposable incomes).

Industry/Entity Type

Massage

Contact Information for Business Card

Rosa Pell Therapies, Tel: 07700 900482, email: lumacrest@postvane.com, (on back of card I want: Rosalind Pell BScHons, CPWRA, RGPC.)

Requirements
Nice to have
• A logo for Rosa Pell Therapies would be good.

```html
<!DOCTYPE html>
<html lang="en">
<head>
<meta charset="utf-8">
<title>Rosa Pell Therapies – Business Card</title>
<link href="https://fonts.googleapis.com/css2?family=Italianno&family=Montserrat:wght@300;400;700&display=swap" rel="stylesheet">
<style>
  :root {
    --page-bg: #e9e9ec;
    --green: #84c441;
    --green-light: #a3d66e;
    --purple: #55237f;
    --purple-light: #7a4ba3;
    --ink-purple: #5a2a8c;
    --white: #ffffff;
    --script: "Italianno", cursive;
    --sans: "Montserrat", Arial, sans-serif;
  }
  * { box-sizing: border-box; margin: 0; padding: 0; }
  html, body {
    width: 1037px;
    height: 1200px;
    overflow: hidden;
    background: var(--page-bg);
  }
  .card {
    position: absolute;
    left: 154px;
    width: 728px;
    height: 433px;
    overflow: hidden;
  }
  .card--back { top: 120px; background: var(--green); }
  .card--front { top: 646px; background: var(--purple); }

  .pattern-band {
    position: absolute;
    left: 0; top: 0;
    width: 100%;
    height: 62%;
  }
  .card--back .pattern-band {
    background: linear-gradient(to bottom, var(--green-light) 0%, rgba(163,214,110,0) 100%);
  }
  .card--front .pattern-band {
    height: 50%;
    background: linear-gradient(to bottom, var(--purple-light) 0%, rgba(122,75,163,0) 100%);
  }

  .holder {
    position: absolute;
    right: 110px;
    top: 282px;
    text-align: right;
    color: var(--ink-purple);
  }
  .holder__name {
    font-family: var(--script);
    font-size: 68px;
    line-height: 1;
  }
  .holder__credentials {
    font-family: var(--sans);
    font-weight: 700;
    font-size: 15px;
    margin-top: 2px;
  }

  .brand {
    position: absolute;
    left: 0; width: 100%;
    top: 160px;
    text-align: center;
    color: var(--white);
  }
  .brand__name {
    display: inline-block;
    font-family: var(--script);
    font-size: 96px;
    line-height: 0.9;
  }
  .brand__tagline {
    display: block;
    font-family: var(--sans);
    font-weight: 300;
    font-size: 24px;
    letter-spacing: 3px;
    margin: 4px 0 0 120px;
  }

  .contact {
    position: absolute;
    left: 250px;
    top: 322px;
    list-style: none;
    color: var(--white);
    font-family: var(--sans);
    font-size: 17px;
  }
  .contact__item {
    display: flex;
    align-items: center;
    gap: 10px;
    height: 30px;
  }
  .contact__icon { width: 17px; height: 17px; flex: none; }
</style>
</head>
<body>
  <section class="card card--back" aria-label="Card back">
    <div class="pattern-band" role="img" aria-label="Soft checkered pattern fading down from the top edge"></div>
    <div class="holder">
      <p class="holder__name">Rosalind Pell</p>
      <p class="holder__credentials">BScHons, CPWRA, RGPC</p>
    </div>
  </section>

  <section class="card card--front" aria-label="Card front">
    <div class="pattern-band" role="img" aria-label="Soft checkered pattern fading down from the top edge"></div>
    <div class="brand">
      <h1 class="brand__name">Rosa Pell</h1>
      <span class="brand__tagline">THERAPIES</span>
    </div>
    <ul class="contact">
      <li class="contact__item">
        <svg class="contact__icon" viewBox="0 0 20 20" aria-hidden="true">
          <rect x="0.5" y="0.5" width="19" height="19" rx="5" fill="#fff"/>
          <path d="M6 4.5c.6 0 1 .4 1.3 1l.8 2c.2.5 0 1-.4 1.3l-.8.6c.7 1.5 1.8 2.6 3.3 3.3l.6-.8c.3-.4.8-.6 1.3-.4l2 .8c.6.3 1 .7 1 1.3 0 1.4-1.1 2.4-2.5 2.4C7.9 16 4 12.1 4 7c0-1.4 1-2.5 2-2.5z" fill="var(--purple)"/>
        </svg>
        <span>07700 900482</span>
      </li>
      <li class="contact__item">
        <svg class="contact__icon" viewBox="0 0 20 20" aria-hidden="true">
          <rect x="0.5" y="0.5" width="19" height="19" rx="5" fill="#fff"/>
          <rect x="4" y="6" width="12" height="8.5" rx="1" fill="none" stroke="var(--purple)" stroke-width="1.4"/>
          <path d="M4.5 6.8l5.5 4 5.5-4" fill="none" stroke="var(--purple)" stroke-width="1.4"/>
        </svg>
        <span>lumacrest@postvane.com</span>
      </li>
    </ul>
  </section>
</body>
</html>
```